Flyer for a Business Consultant

I need a one-page description of services. I am a Brennick Certifed Talents Mentor. I do not have a personal website but think I will soon purchase this template https://varlowskins.example/skins/lectern/. I like the larger font, simplicity and larger font. I will attach his pricing flyer which I like - not to overly guide or restrict your creative thinking, but only to give a little perspective. I don't like busy, noisy - I like clarity, simplicity. Here 's the Brennick website which these same traits https://www.brennicktalentshub.example/ and can be a source of ideas and colors.

Target Market(s)

CEOs and Middle Managers in organizations

Industry/Entity Type

Financial Service

Colors

Designer to choose colors to be used in the design.

Requirements
Must have
• Clarity, simplicity, but also strength (not weak or frilly looking)
Nice to have
• Warm color(s), larger/not skinny font
Should not have
• Loud, noisy, busy

```html
<!DOCTYPE html>
<html lang="en">
<head>
<meta charset="utf-8">
<title>Strength-Based Team Effectiveness Flyer</title>
<link href="https://fonts.googleapis.com/css2?family=Bebas+Neue&family=Lato:ital,wght@0,400;0,700;1,400;1,700&display=swap" rel="stylesheet">
<style>
  :root {
    --green: #1d7a3e;
    --green-dark: #0f5a2b;
    --charcoal: #2e2e2e;
    --charcoal-mid: #555555;
    --pill: #333333;
    --text-light: #f2f2f2;
    --text-dark: #2a2a2a;
    --grey-text: #6b6b6b;
    --white: #ffffff;
    --photo-light: #e9e9e9;
    --photo-mid: #cfcfcf;
  }
  * { box-sizing: border-box; margin: 0; padding: 0; }
  html, body { width: 902px; height: 1200px; overflow: hidden; background: var(--white); }
  .flyer { position: relative; width: 902px; height: 1200px; font-family: 'Lato', sans-serif; color: var(--text-dark); overflow: hidden; }

  .header { position: absolute; left: 0; top: 0; width: 902px; height: 226px; background: var(--green); text-align: center; color: var(--white); font-family: 'Bebas Neue', sans-serif; }
  .header__line { display: block; line-height: 1; }
  .header__line--one { font-size: 66px; padding-top: 38px; }
  .header__line--two { font-size: 60px; margin-top: 22px; }

  .intro { position: absolute; left: 0; top: 226px; width: 902px; height: 216px; background: var(--white); }
  .intro__photo { position: absolute; right: 0; top: 0; width: 500px; height: 216px; background: linear-gradient(90deg, var(--white) 0%, var(--photo-light) 40%, var(--photo-mid) 100%); opacity: .8; }
  .intro__pill { position: absolute; left: 218px; top: -22px; width: 472px; height: 50px; border-radius: 25px; background: var(--pill); border: 2px solid var(--white); color: var(--white); font-family: 'Bebas Neue', sans-serif; font-size: 32px; line-height: 48px; text-align: center; }
  .intro__list { position: absolute; left: 40px; top: 72px; list-style: none; }
  .intro__list li { position: relative; padding-left: 33px; font-size: 17.5px; font-weight: 700; font-style: italic; line-height: 33px; color: var(--text-dark); }
  .intro__list li::before { content: ""; position: absolute; left: 2px; top: 11px; width: 12px; height: 12px; border-radius: 50%; background: var(--text-dark); }

  .services { position: absolute; left: 0; top: 442px; width: 902px; height: 384px; background: radial-gradient(ellipse at 50% 60%, var(--charcoal-mid) 0%, var(--charcoal) 65%); }
  .service__tab { position: absolute; top: 0; height: 86px; background: var(--green); color: var(--white); font-family: 'Bebas Neue', sans-serif; text-align: center; line-height: 1; }
  .service__tab svg { position: absolute; top: 0; }
  .service__tab-main { display: block; font-size: 42px; padding-top: 10px; }
  .service__tab-sub { display: block; font-size: 28px; margin-top: 4px; }
  .service__tab--discovery .service__tab-main { font-size: 30px; padding-top: 14px; }
  .service__tab--discovery .service__tab-sub { font-size: 30px; margin-top: 8px; }
  .service__tab--individual { left: 57px; width: 190px; }
  .service__tab--discovery { left: 322px; width: 238px; }
  .service__tab--followon { left: 617px; width: 224px; }

  .service__text { position: absolute; top: 113px; color: var(--text-light); font-size: 15.5px; line-height: 20.5px; text-align: justify; hyphens: auto; }
  .service__text--individual { left: 49px; width: 240px; }
  .service__text--discovery { left: 337px; width: 243px; }
  .service__text--followon { left: 620px; width: 242px; }
  .service__divider { position: absolute; top: 113px; width: 1px; height: 232px; background: #8a8a8a; }
  .service__divider--a { left: 322px; }
  .service__divider--b { left: 600px; }

  .contact { position: absolute; left: 0; top: 826px; width: 902px; height: 374px; background: var(--white); }
  .contact__badge { position: absolute; left: 45px; top: 27px; width: 413px; height: 108px; border: 2px solid #9a9a9a; display: flex; align-items: center; padding-left: 18px; gap: 20px; }
  .contact__badge-mark { width: 44px; height: 66px; background: #8c8c8c; flex: none; }
  .contact__badge-name { font-size: 24px; font-weight: 400; color: #555555; line-height: 1.2; }
  .contact__cta { position: absolute; left: 482px; top: 52px; font-family: 'Bebas Neue', sans-serif; font-size: 58px; line-height: 1; color: var(--grey-text); white-space: nowrap; }
  .contact__cta-accent { color: var(--green); }
  .contact__photo { position: absolute; left: 0; top: 156px; width: 474px; height: 218px; background: linear-gradient(180deg, var(--photo-light) 0%, var(--photo-mid) 100%); }
  .contact__card { position: absolute; left: 474px; top: 156px; width: 428px; height: 218px; background: var(--green); color: var(--white); padding: 20px 0 0 26px; }
  .contact__name { font-size: 29px; font-weight: 700; line-height: 1.2; }
  .contact__role { font-size: 19px; font-weight: 700; font-style: italic; margin-top: 8px; }
  .contact__row { display: flex; align-items: center; gap: 10px; margin-top: 18px; font-size: 19px; font-weight: 700; }
  .contact__row--phone { margin-top: 8px; font-size: 35px; }
</style>
</head>
<body>
<main class="flyer">
  <header class="header">
    <span class="header__line header__line--one">A Strength-Based Approach</span>
    <span class="header__line header__line--two">To Managing Team Effectiveness</span>
  </header>

  <section class="intro">
    <div class="intro__photo" role="img" aria-label="Faded photo of business colleagues talking in a meeting"></div>
    <div class="intro__pill">We Help Teams Grow Stronger By:</div>
    <ul class="intro__list">
      <li>Bringing a deep awareness of their strengths and the strengths of their associates.</li>
      <li>Increasing the Team’s communication and sense of partnership.</li>
      <li>Improving employee engagement and effectiveness.</li>
    </ul>
  </section>

  <section class="services">
    <div class="service__tab service__tab--individual">
      <svg width="14" height="26" style="left:-14px" viewBox="0 0 14 26"><polygon points="14,0 0,26 14,26" fill="var(--green-dark)"/></svg>
      <svg width="14" height="26" style="right:-14px" viewBox="0 0 14 26"><polygon points="0,0 14,26 0,26" fill="var(--green-dark)"/></svg>
      <span class="service__tab-main">Individual</span>
      <span class="service__tab-sub">Sessions</span>
    </div>
    <div class="service__tab service__tab--discovery">
      <svg width="14" height="26" style="left:-14px" viewBox="0 0 14 26"><polygon points="14,0 0,26 14,26" fill="var(--green-dark)"/></svg>
      <svg width="14" height="26" style="right:-14px" viewBox="0 0 14 26"><polygon points="0,0 14,26 0,26" fill="var(--green-dark)"/></svg>
      <span class="service__tab-main">Strength Discovery</span>
      <span class="service__tab-sub">Workshop</span>
    </div>
    <div class="service__tab service__tab--followon">
      <svg width="14" height="26" style="left:-14px" viewBox="0 0 14 26"><polygon points="14,0 0,26 14,26" fill="var(--green-dark)"/></svg>
      <svg width="14" height="26" style="right:-14px" viewBox="0 0 14 26"><polygon points="0,0 14,26 0,26" fill="var(--green-dark)"/></svg>
      <span class="service__tab-main">Follow-On</span>
      <span class="service__tab-sub">Modules</span>
    </div>

    <p class="service__text service__text--individual">Conversational feedback and coaching sessions based on Brennick’s TalentPrism assessments. These sessions last about an hour and lead to a personalized translation of the results and how their strengths show up in their work and inherent blind spots they bring.</p>
    <div class="service__divider service__divider--a"></div>
    <p class="service__text service__text--discovery">A retreat-style Team Workshop in which the team learns each other’s unique Top 5 strengths. The session is very interactive and provides a common language that leads to improved communication and effectiveness. Tailored in 2, 3 and 4-hour options are tailored to your Team’s challenges and opportunities.</p>
    <div class="service__divider service__divider--b"></div>
    <p class="service__text service__text--followon">Follow-on is important to make the insights learned to be practical and integrated into the Teams’ approach and workflows.<br>In a debrief session included as part of the workshop, we provide several 15-minute exercise modules for use in regular meetings, and we offer guest facilitated modules of 30-60 minutes each.</p>
  </section>

  <section class="contact">
    <div class="contact__badge">
      <div class="contact__badge-mark"></div>
      <div class="contact__badge-name">Brennick Certifed<br>Talents Mentor</div>
    </div>
    <div class="contact__cta">Contact Me <span class="contact__cta-accent">Today!</span></div>
    <div class="contact__photo" role="img" aria-label="Faded photo of a businesswoman on the phone and colleagues shaking hands"></div>
    <div class="contact__card">
      <div class="contact__name">Marcus Ellery</div>
      <div class="contact__role">Brennick Workplace Talents Mentor</div>
      <div class="contact__row">
        <svg width="20" height="14" viewBox="0 0 20 14" aria-hidden="true"><rect x="1" y="1" width="18" height="12" fill="none" stroke="#fff" stroke-width="2"/><polyline points="1,1 10,8 19,1" fill="none" stroke="#fff" stroke-width="2"/></svg>
        <span>marcus@talentsiq.example</span>
      </div>
      <div class="contact__row contact__row--phone">
        <svg width="22" height="22" viewBox="0 0 22 22" aria-hidden="true"><circle cx="11" cy="11" r="9.5" fill="none" stroke="#fff" stroke-width="2"/><path d="M7.5 6.5c.6-.6 1.3-.5 1.7.1l.9 1.4c.3.5.2 1-.2 1.4l-.5.5c.6 1.3 1.6 2.3 2.9 2.9l.5-.5c.4-.4.9-.5 1.4-.2l1.4.9c.6.4.7 1.1.1 1.7-1 1-2.6 1.2-4 .4-2-1.1-3.6-2.7-4.7-4.7-.8-1.4-.6-3 .5-3.9z" fill="#fff"/></svg>
        <span>555-014-2286</span>
      </div>
    </div>
  </section>
</main>
</body>
</html>
```